We have a parent company, Summit Harbor Group (SHG), that has other company partners. We are looking for ways to incorporate our SHG logo with our network partners, Beacon Ledger and The Blue Gate. My initial thought is to have SHG as front of card logo, and include The Blue Gate and Beacon Ledger logos on back but I'm open to ideas. Card should include website www.summitharborgrp.example (use for reference). Keywords "Tax Services" "Real Estate" "Insurance" "Investments" "Chief Financial Officer"

Industry/Entity Type

Financial

```html
<!DOCTYPE html>
<html lang="en">
<head>
<meta charset="utf-8">
<title>Summit Harbor Group – Business Card</title>
<link href="https://fonts.googleapis.com/css2?family=Lato:wght@400;700&display=swap" rel="stylesheet">
<style>
  :root {
    --brand-red: #e8242b;
    --brand-blue: #1256a6;
    --paper: #ffffff;
    --backdrop: #3a3a3a;
    --badge-grey: #e4e2df;
  }
  * { margin: 0; padding: 0; box-sizing: border-box; }
  html, body { width: 1200px; height: 750px; overflow: hidden; }
  body {
    background: var(--backdrop);
    font-family: "Lato", Arial, sans-serif;
    position: relative;
  }
  .card {
    position: absolute;
    width: 466px;
    height: 266px;
    background: var(--paper);
    overflow: hidden;
  }
  .card--front { left: 367px; top: 93px; }
  .card--back { left: 368px; top: 406px; }

  .accent-band { position: absolute; left: 0; bottom: 0; width: 100%; height: 18px; }

  .wordmark {
    color: var(--brand-blue);
    font-weight: 700;
    letter-spacing: 0.04em;
    text-transform: uppercase;
    display: flex;
    align-items: center;
    gap: 8px;
    white-space: nowrap;
  }
  .wordmark__dot {
    width: 14px; height: 14px; border-radius: 50%;
    background: var(--brand-red);
  }
  .card--front .wordmark {
    position: absolute; left: 0; right: 0; top: 132px;
    justify-content: center; font-size: 22px;
  }
  .services {
    position: absolute; left: 0; right: 0; top: 204px;
    text-align: center; color: var(--brand-blue); font-size: 12.5px;
  }

  .holder { position: absolute; left: 25px; top: 28px; }
  .holder__name { color: var(--brand-blue); font-weight: 700; font-size: 14px; line-height: 1.1; }
  .holder__role { color: var(--brand-red); font-size: 12px; line-height: 1; }
  .edge-tab {
    position: absolute; left: -12px; top: 38px;
    width: 24px; height: 24px; border-radius: 50%; background: var(--brand-red);
  }
  .card--back .wordmark {
    position: absolute; right: 24px; top: 84px; font-size: 16px; gap: 6px;
  }
  .card--back .wordmark__dot { width: 11px; height: 11px; }

  .contact-list {
    position: absolute; left: 30px; top: 168px; list-style: none;
    color: var(--brand-blue); font-size: 12px;
  }
  .contact-list li { display: flex; align-items: center; gap: 6px; height: 16.4px; }
  .contact-list svg { width: 14px; height: 14px; flex: none; }

  .partner {
    position: absolute; right: 25px;
    font-weight: 700; color: var(--brand-red);
  }
  .partner--ledger { top: 160px; font-size: 13px; text-transform: uppercase; letter-spacing: 0.02em; }
  .partner--gate {
    top: 185px; width: 130px; height: 47px;
    background: var(--badge-grey);
    display: flex; align-items: center; justify-content: center;
    font-size: 13px;
  }
</style>
</head>
<body>

<section class="card card--front">
  <div class="wordmark"><span class="wordmark__dot"></span>Summit Harbor Group</div>
  <p class="services">Tax Services | Real Estate | Insurance | Investments | Chief Financial Officer</p>
  <svg class="accent-band" viewBox="0 0 466 18" preserveAspectRatio="none">
    <polygon points="0,0 233,0 224,18 0,18" fill="var(--brand-red)"/>
    <polygon points="240,0 466,0 466,18 231,18" fill="var(--brand-blue)"/>
  </svg>
</section>

<section class="card card--back">
  <span class="edge-tab"></span>
  <div class="holder">
    <p class="holder__name">JORDAN HALE</p>
    <p class="holder__role">Owner</p>
  </div>

  <div class="wordmark"><span class="wordmark__dot"></span>Summit Harbor Group</div>

  <ul class="contact-list">
    <li>
      <svg viewBox="0 0 14 14"><circle cx="7" cy="7" r="6.3" fill="none" stroke="var(--brand-red)" stroke-width="1.2"/><path d="M4 5.2c0-.8 1-1.4 3-1.4s3 .6 3 1.4v.6H8.7v-.8H5.3v.8H4zM4.6 6.5h4.8l.6 3.5H4z" fill="var(--brand-red)"/></svg>
      555-014-2276
    </li>
    <li>
      <svg viewBox="0 0 14 14"><circle cx="7" cy="7" r="6.3" fill="none" stroke="var(--brand-red)" stroke-width="1.2"/><rect x="3.8" y="4.8" width="6.4" height="4.4" fill="var(--brand-red)"/><path d="M3.8 4.8 7 7.3l3.2-2.5" fill="none" stroke="#fff" stroke-width=".8"/></svg>
      hello@summitharbor.example
    </li>
    <li>
      <svg viewBox="0 0 14 14"><circle cx="7" cy="7" r="6.3" fill="none" stroke="var(--brand-red)" stroke-width="1.2"/><circle cx="7" cy="7" r="3.4" fill="none" stroke="var(--brand-red)" stroke-width=".9"/><path d="M3.6 7h6.8M7 3.6v6.8" stroke="var(--brand-red)" stroke-width=".8"/></svg>
      www.summitharborgrp.example
    </li>
    <li>
      <svg viewBox="0 0 14 14"><circle cx="7" cy="7" r="6.3" fill="none" stroke="var(--brand-red)" stroke-width="1.2"/><path d="M7 11 4.6 7.3A2.6 2.6 0 1 1 9.4 7.3z" fill="none" stroke="var(--brand-red)" stroke-width="1"/><circle cx="7" cy="6" r=".9" fill="var(--brand-red)"/></svg>
      1420 Ridgeview Ave, Lakeside, CO 80000
    </li>
  </ul>

  <div class="partner partner--ledger">Beacon Ledger</div>
  <div class="partner partner--gate">The Blue Gate</div>

  <svg class="accent-band" viewBox="0 0 466 18" preserveAspectRatio="none">
    <polygon points="0,0 233,0 224,18 0,18" fill="var(--brand-red)"/>
    <polygon points="240,0 466,0 466,18 231,18" fill="var(--brand-blue)"/>
  </svg>
</section>

</body>
</html>
```